Graphic Design for MARKETING BROCHURE -Cedarwood Knoll Estate- Wedding Specific -Media Kit for print

220 acres estate that provides high-end wedding and corporate sponsored venues throughout the property. 14,000 sf estate mansion allows for sunken garden, [login to view URL] size swimming pool, breathtaking views, wine tasting, etc. We are developing our 1st phase wedding marketing material to attract wedding coordinators, event coordinators, brides, corporate sponsor, etc

```html
<!DOCTYPE html>
<html lang="en">
<head>
<meta charset="utf-8">
<title>Cedarwood Knoll Estate – Wedding Brochure</title>
<link href="https://fonts.googleapis.com/css2?family=Cinzel:wght@400&family=Cormorant+Garamond:ital,wght@1,500&family=Libre+Baskerville:wght@400;700&display=swap" rel="stylesheet">
<style>
  :root{
    --page:#ffffff;
    --ink:#1b1a19;
    --gold:#c9a24b;
    --gold-light:#f1d88a;
    --gold-deep:#9c7424;
    --copy:#d6d0c4;
    --copy-dim:#a9a398;
  }
  *{box-sizing:border-box;margin:0;padding:0}
  html,body{width:719px;height:1200px;overflow:hidden;background:var(--page)}
  .canvas{position:relative;width:719px;height:1200px}
  .spread{position:absolute;left:40px;width:639px;background:var(--ink);box-shadow:0 4px 8px rgba(0,0,0,.35);overflow:hidden}
  .spread--cover{top:70px;height:272px}
  .spread--inside{top:379px;height:270px}
  .photo{position:absolute}
  .copy{position:absolute;font-family:"Libre Baskerville",serif;font-size:3.9px;line-height:5px;color:var(--copy);text-align:justify}
  .copy p+p{margin-top:3px}
  .copy b{font-weight:700}
  .heading{position:absolute;font-family:"Cinzel",serif;font-size:6px;color:var(--copy);letter-spacing:.2px;white-space:nowrap}
  .brand{position:absolute;font-family:"Cinzel",serif;color:var(--gold);text-align:center;white-space:nowrap;letter-spacing:.6px}
  .brand__name{font-size:10px;line-height:11px}
  .brand__sub{font-size:4.5px;letter-spacing:1.6px;border-top:.5px solid var(--gold);margin-top:2px;padding-top:1px}
  .brand--small .brand__name{font-size:7px;line-height:8px;letter-spacing:.4px}
  .brand--small .brand__sub{font-size:3.6px}
  .contact{position:absolute;font-family:"Libre Baskerville",serif;font-size:4.3px;line-height:6px;color:var(--copy);text-align:center;white-space:nowrap}
  .web{position:absolute;font-family:"Libre Baskerville",serif;font-size:4px;color:var(--copy-dim);white-space:nowrap}
  .tagline{position:absolute;font-family:"Cormorant Garamond",serif;font-style:italic;font-weight:500;font-size:12px;color:var(--gold);white-space:nowrap}
  .gold-band{position:absolute;background:linear-gradient(90deg,var(--gold-deep),var(--gold-light) 45%,var(--gold))}
  .gold-band__label{font-family:"Cinzel",serif;font-size:7px;color:var(--ink);text-align:right;padding-right:6px;line-height:13px;white-space:nowrap}
  .label-band{position:absolute;background:linear-gradient(90deg,var(--gold-light),var(--gold));font-family:"Cinzel",serif;font-size:6px;color:var(--ink);text-align:center;line-height:10px}
  .ornament{position:absolute;background:radial-gradient(ellipse at 55% 50%,rgba(216,178,92,.85) 0%,rgba(176,134,52,.55) 40%,rgba(27,26,25,0) 72%)}
</style>
</head>
<body>
<main class="canvas">

  <section class="spread spread--cover">
    <div class="photo" style="left:0;top:0;width:214px;height:272px;background:linear-gradient(180deg,#eef2ea 0%,#c8d6b0 28%,#a4b24a 45%,#6d7b2c 62%,#8a6a45 78%,#6e5236 100%)" role="img" aria-label="Wooden deck with a bistro table and chairs overlooking a misty cornfield"></div>

    <div class="brand" style="left:260px;top:44px;width:120px">
      <div class="brand__name">Cedarwood Knoll</div>
      <div class="brand__sub">ESTATE</div>
    </div>
    <div class="copy" style="left:254px;top:78px;width:132px">
      <p>Set among rolling hills and quiet woodland, our estate welcomes couples and guests for weddings, receptions and gatherings. Every detail is shaped with care, from the first tour to the final dance.</p>
    </div>
    <div class="photo" style="left:260px;top:131px;width:121px;height:65px;background:linear-gradient(135deg,#ecebe6,#dcdad2)" role="img" aria-label="Location map of roads around the estate"></div>
    <div class="contact" style="left:234px;top:208px;width:172px">
      T: 555-014-2201 &nbsp;C: 555-014-3388 &nbsp;F: 555-014-2290<br>
      2750 OLD MILL ROAD, HARLOW, INDIANA 47000
    </div>
    <div class="web" style="left:285px;top:247px">www.cedarwoodknollestate.com</div>

    <div class="ornament" style="left:428px;top:34px;width:200px;height:200px" role="img" aria-label="Large gold swirl ornament"></div>
    <div class="brand brand--small" style="left:548px;top:26px;width:80px">
      <div class="brand__name">Cedarwood Knoll</div>
      <div class="brand__sub">ESTATE</div>
    </div>
    <div class="tagline" style="right:12px;top:242px">…for that Special Occasion</div>
  </section>

  <section class="spread spread--inside">
    <div class="photo" style="left:0;top:0;width:214px;height:98px;background:linear-gradient(180deg,#8fb0d8 0%,#c9d7e4 35%,#3f5a2c 60%,#4f7a2e 100%)" role="img" aria-label="Estate mansion at dusk behind a wide lawn"></div>
    <div class="gold-band" style="left:0;top:98px;width:214px;height:13px"><div class="gold-band__label">SOMETHING ABOUT CEDARWOOD KNOLL</div></div>
    <div class="copy" style="left:10px;top:120px;width:124px">
      <p><b>Our grounds offer</b> sweeping lawns, a sunken garden and shaded paths, giving every celebration a natural and elegant setting for guests to enjoy.</p>
      <p>The mansion hosts intimate dinners and grand receptions alike, with spacious halls, warm lighting and a team ready to help plan each moment.</p>
    </div>
    <div class="photo" style="left:140px;top:120px;width:64px;height:46px;background:linear-gradient(135deg,#6e5a38,#d8cfa8 55%,#4a3b22)" role="img" aria-label="Spa still life with a white flower"></div>
    <div class="heading" style="left:140px;top:170px">Some Text here</div>
    <div class="copy" style="left:140px;top:178px;width:66px">
      <p>Wine tastings, poolside evenings and open views across the valley make every stay memorable.</p>
      <p>Wine tastings, poolside evenings and open views across the valley make every stay memorable.</p>
    </div>
    <div class="gold-band" style="left:0;top:190px;width:10px;height:47px"></div>
    <div class="photo" style="left:10px;top:190px;width:125px;height:47px;background:linear-gradient(180deg,#9fc0e4 0%,#cfe0ee 30%,#4e7e2c 55%,#6d9a34 100%)" role="img" aria-label="Green rolling hills with trees"></div>
    <div class="copy" style="left:10px;top:242px;width:124px">
      <p>Open views across the valley and quiet woodland paths frame every gathering.</p>
    </div>

    <div class="heading" style="left:222px;top:10px">Some Text Here</div>
    <div class="copy" style="left:222px;top:19px;width:110px">
      <p>Our grounds offer sweeping lawns, a sunken garden and shaded paths, giving every celebration a natural and elegant setting for guests to enjoy.</p>
      <p>The mansion hosts intimate dinners and grand receptions alike, with spacious halls, warm lighting and a team ready to help plan each moment.</p>
    </div>
    <div class="photo" style="left:338px;top:11px;width:80px;height:91px;background:linear-gradient(180deg,#f2efe6,#d9d3c2 60%,#9d8f70)" role="img" aria-label="Reception tables set with white linen and centrepieces"></div>
    <div class="photo" style="left:222px;top:112px;width:88px;height:146px;background:linear-gradient(180deg,#5d8a3a 0%,#a9c984 30%,#e8f1ec 50%,#4d7a2a 80%,#3c5e22 100%)" role="img" aria-label="Large tree framing a meadow with a wooden fence"></div>
    <div class="heading" style="left:317px;top:115px">Some Text here</div>
    <div class="copy" style="left:317px;top:124px;width:105px">
      <p>The mansion hosts intimate dinners and grand receptions alike, with spacious halls, warm lighting and a team ready to help plan each moment.</p>
      <p>Wine tastings, poolside evenings and open views across the valley make every stay memorable.</p>
    </div>
    <div class="photo" style="left:310px;top:207px;width:112px;height:51px;background:linear-gradient(180deg,#4a6a34,#2f6b75 55%,#58b5d6 80%,#8a8b7c)" role="img" aria-label="Swimming pool surrounded by trees and lounge chairs"></div>

    <div class="heading" style="left:436px;top:10px">Some Text here</div>
    <div class="copy" style="left:436px;top:19px;width:100px">
      <p>Our grounds offer sweeping lawns, a sunken garden and shaded paths, giving every celebration a natural and elegant setting for guests to enjoy.</p>
      <p>The mansion hosts intimate dinners and grand receptions alike, with spacious halls, warm lighting and a team ready to help plan each moment.</p>
    </div>
    <div class="photo" style="left:426px;top:102px;width:108px;height:53px;background:linear-gradient(180deg,#f5e2a8 0%,#c89a4a 40%,#4e6a28 75%,#2f4a1c)" role="img" aria-label="Couple walking toward an outdoor reception at sunset"></div>
    <div class="copy" style="left:436px;top:160px;width:100px">
      <p>Our grounds offer sweeping lawns, a sunken garden and shaded paths, giving every celebration a natural and elegant setting for guests to enjoy.</p>
    </div>
    <div class="copy" style="left:436px;top:190px;width:100px">
      <p>Wine tastings, poolside evenings and open views across the valley make every stay memorable.</p>
    </div>
    <div class="photo" style="left:426px;top:207px;width:108px;height:51px;background:linear-gradient(180deg,#3a5a22,#6f8f3e 45%,#b4b7a6 70%,#4a5a2a)" role="img" aria-label="Tree-lined driveway leading to the estate"></div>

    <div class="label-band" style="left:542px;top:8px;width:97px;height:10px">SOME TEXT</div>
    <div class="photo" style="left:542px;top:18px;width:97px;height:167px;background:linear-gradient(180deg,#d9c39a 0%,#a88c5e 35%,#e2d2b4 60%,#c3ad88 100%)" role="img" aria-label="Banquet hall with long dressed tables and tall floral centrepieces"></div>
    <div class="photo" style="left:542px;top:185px;width:97px;height:73px;background:linear-gradient(135deg,#4a3e28,#c9d3a8 50%,#f1f2e4 65%,#3b3222)" role="img" aria-label="White rose and hydrangea table arrangement"></div>
  </section>

</main>
</body>
</html>
```